Veterinary hospital brochure design

we need brochure design for our veterinary hospital, something interesting, catchy and unique. Once we get going we need to add few unique services we offer and should be highlighted.Nice colors, and should be very professional looking. Brochure to be tri fold, nice colors highlight our services.
Like shades of blues or green.This is full service veterinary hospital. We do focus and specialize in Canine reproduction.

pet owners

Hospital

Serif
Script

• catchy words
• unique design
• have our unique services included
• good pictures and catchy words etc etc

```html
<!DOCTYPE html>
<html lang="en">
<head>
<meta charset="utf-8">
<title>Brookfield Veterinary Specialists – Tri-fold Brochure</title>
<link href="https://fonts.googleapis.com/css2?family=Open+Sans:ital,wght@0,400;0,600;0,700;1,600;1,700&display=swap" rel="stylesheet">
<style>
  :root{
    --page-bg:#e4e4e4;
    --paper:#ffffff;
    --blue:#1b6ab6;
    --blue-deep:#0b4a93;
    --blue-light:#2f86d0;
    --green:#8cc63f;
    --green-dark:#6fae23;
    --ink:#3a3a3a;
    --photo-warm:#d9a866;
    --photo-warm-2:#b5773a;
    --photo-scrubs:#2f7fcf;
  }
  *{box-sizing:border-box;margin:0;padding:0}
  html,body{width:1200px;height:800px;overflow:hidden}
  body{background:var(--page-bg);font-family:"Open Sans",Arial,sans-serif;color:var(--ink)}
  .brochure{position:absolute;left:45px;top:55px;width:1110px;height:690px;display:flex;box-shadow:0 12px 30px rgba(0,0,0,.18)}
  .panel{position:relative;width:370px;height:690px;overflow:hidden;background:var(--paper)}
  .panel + .panel{border-left:1px solid rgba(0,0,0,.06)}
  .panel-bg{position:absolute;inset:0;width:100%;height:100%}
  .photo{position:absolute}

  /* About panel */
  .about-title{position:absolute;left:34px;top:38px;font-size:22px;font-weight:700;color:var(--blue);letter-spacing:.5px}
  .about-rule{position:absolute;left:34px;top:72px;width:290px;height:2px;background:var(--green)}
  .about-copy{position:absolute;left:34px;top:88px;width:302px;font-size:12.5px;line-height:1.32;text-align:justify}
  .about-copy p{margin-bottom:13px}
  .photo-dog-cat{left:40px;top:370px;width:290px;height:215px;border-radius:48% 52% 30% 30%/55% 55% 25% 25%;background:radial-gradient(ellipse at 40% 40%,#f1d3a1,var(--photo-warm) 55%,var(--photo-warm-2))}

  /* shared bottom band */
  .band-text{position:absolute;bottom:16px;font-size:16px;color:#fff;white-space:nowrap}
  .band-text.emergency{left:28px;font-weight:400}
  .band-text.clinic{left:18px;font-weight:700;font-size:17px}

  /* Services panel */
  .photo-rabbit{left:22px;top:30px;width:118px;height:118px;border-radius:50%;border:5px solid var(--green);background:radial-gradient(circle at 50% 45%,#e6c9a6,#b78557 75%)}
  .photo-puppy{left:150px;top:14px;width:200px;height:150px;border-radius:50% 50% 10% 10%/60% 60% 10% 10%;background:radial-gradient(ellipse at 50% 40%,#e8ab62,#c47a2c 65%)}
  .services-title{position:absolute;left:0;width:100%;top:222px;text-align:center;font-size:20px;font-weight:600;color:var(--green);letter-spacing:.5px}
  .services-list{position:absolute;left:48px;top:266px;list-style:none}
  .services-list li{display:flex;align-items:center;gap:12px;font-size:14.5px;color:#fff;height:30px}
  .services-list svg{width:16px;height:16px;flex:none}

  /* Philosophy panel */
  .photo-pets{left:20px;top:18px;width:335px;height:120px;border-radius:40px 40px 10px 10px;background:linear-gradient(90deg,#b7aa97,#e7ddd3 50%,#6b4a2e)}
  .philosophy-title{position:absolute;left:28px;top:178px;font-size:20px;font-weight:700;font-style:italic;color:var(--green)}
  .philosophy-rule{position:absolute;left:28px;top:210px;width:300px;height:2px;background:var(--green)}
  .philosophy-copy{position:absolute;left:28px;top:222px;width:315px;font-size:12.5px;line-height:1.35;color:#fff;font-style:italic}
  .philosophy-list{list-style:none;margin-top:10px}
  .philosophy-list li::before{content:"• "}
  .photo-vet{right:0;bottom:0;width:330px;height:258px;border-radius:150px 0 0 0;border-top:6px solid var(--green);border-left:6px solid var(--green);background:linear-gradient(160deg,#f1ede8 0%,#5b9ee0 40%,var(--photo-scrubs) 70%,#d9dde2 100%)}
</style>
</head>
<body>
<main class="brochure">

  <!-- About -->
  <section class="panel panel-about">
    <svg class="panel-bg" viewBox="0 0 370 690" preserveAspectRatio="none" aria-hidden="true">
      <path d="M0 520 Q200 560 370 470 L370 690 L0 690Z" fill="var(--blue)"/>
      <path d="M0 515 Q200 555 370 465" fill="none" stroke="var(--green)" stroke-width="5"/>
      <rect x="0" y="628" width="370" height="62" fill="var(--green)"/>
      <rect x="0" y="620" width="370" height="8" fill="var(--blue-deep)"/>
    </svg>
    <h2 class="about-title">ABOUT US</h2>
    <div class="about-rule"></div>
    <div class="about-copy">
      <p>Founded in 1977, Brookfield's preeminent Cedar Ridge Hospital for Animals melds old world values with the latest and most sophisticated high-tech medical equipment and standards.</p>
      <p>Sensitive to even the slightest change, your pet will appreciate having just one familiar locale for all of his or her care needs – from vaccinations to wellness examinations, laser surgery to critical care, grooming to dental care, and daycare to long-term boarding.</p>
      <p>Find comfort within our warm and welcoming environment and in a space that makes your pet feel relaxed and adored from the moment they step through our door.</p>
    </div>
    <div class="photo photo-dog-cat" role="img" aria-label="Photo of a golden retriever lying down with an orange kitten nestled against it"></div>
    <p class="band-text emergency">For emergency pet care, please contact</p>
  </section>

  <!-- Services -->
  <section class="panel panel-services">
    <svg class="panel-bg" viewBox="0 0 370 690" preserveAspectRatio="none" aria-hidden="true">
      <path d="M0 120 Q40 150 60 175 L185 200 L370 150 L370 690 L0 690Z" fill="var(--blue)"/>
      <path d="M60 175 L185 200 L370 150" fill="none" stroke="var(--green)" stroke-width="5"/>
      <rect x="0" y="628" width="370" height="62" fill="var(--green)"/>
      <rect x="0" y="620" width="370" height="8" fill="var(--blue-deep)"/>
    </svg>
    <div class="photo photo-puppy" role="img" aria-label="Photo of a smiling golden labrador puppy"></div>
    <div class="photo photo-rabbit" role="img" aria-label="Round photo of a lop-eared rabbit"></div>
    <h2 class="services-title">OUR SERVICES</h2>
    <ul class="services-list">
      <li><svg viewBox="0 0 16 16"><g fill="var(--green)"><circle cx="8" cy="11" r="3.6"/><circle cx="3" cy="6.5" r="1.8"/><circle cx="6.3" cy="3.4" r="1.8"/><circle cx="9.7" cy="3.4" r="1.8"/><circle cx="13" cy="6.5" r="1.8"/></g></svg>Breeding Sounds Exams</li>
      <li><svg viewBox="0 0 16 16"><g fill="var(--green)"><circle cx="8" cy="11" r="3.6"/><circle cx="3" cy="6.5" r="1.8"/><circle cx="6.3" cy="3.4" r="1.8"/><circle cx="9.7" cy="3.4" r="1.8"/><circle cx="13" cy="6.5" r="1.8"/></g></svg>Semen Collections</li>
      <li><svg viewBox="0 0 16 16"><g fill="var(--green)"><circle cx="8" cy="11" r="3.6"/><circle cx="3" cy="6.5" r="1.8"/><circle cx="6.3" cy="3.4" r="1.8"/><circle cx="9.7" cy="3.4" r="1.8"/><circle cx="13" cy="6.5" r="1.8"/></g></svg>Computer Assisted Semen Analysis</li>
      <li><svg viewBox="0 0 16 16"><g fill="var(--green)"><circle cx="8" cy="11" r="3.6"/><circle cx="3" cy="6.5" r="1.8"/><circle cx="6.3" cy="3.4" r="1.8"/><circle cx="9.7" cy="3.4" r="1.8"/><circle cx="13" cy="6.5" r="1.8"/></g></svg>Caesarian Sections</li>
      <li><svg viewBox="0 0 16 16"><g fill="var(--green)"><circle cx="8" cy="11" r="3.6"/><circle cx="3" cy="6.5" r="1.8"/><circle cx="6.3" cy="3.4" r="1.8"/><circle cx="9.7" cy="3.4" r="1.8"/><circle cx="13" cy="6.5" r="1.8"/></g></svg>Ovulation Timing</li>
      <li><svg viewBox="0 0 16 16"><g fill="var(--green)"><circle cx="8" cy="11" r="3.6"/><circle cx="3" cy="6.5" r="1.8"/><circle cx="6.3" cy="3.4" r="1.8"/><circle cx="9.7" cy="3.4" r="1.8"/><circle cx="13" cy="6.5" r="1.8"/></g></svg>Infertility Work-Ups</li>
      <li><svg viewBox="0 0 16 16"><g fill="var(--green)"><circle cx="8" cy="11" r="3.6"/><circle cx="3" cy="6.5" r="1.8"/><circle cx="6.3" cy="3.4" r="1.8"/><circle cx="9.7" cy="3.4" r="1.8"/><circle cx="13" cy="6.5" r="1.8"/></g></svg>Transcervical Insemination</li>
      <li><svg viewBox="0 0 16 16"><g fill="var(--green)"><circle cx="8" cy="11" r="3.6"/><circle cx="3" cy="6.5" r="1.8"/><circle cx="6.3" cy="3.4" r="1.8"/><circle cx="9.7" cy="3.4" r="1.8"/><circle cx="13" cy="6.5" r="1.8"/></g></svg>Surgical Insemination</li>
      <li><svg viewBox="0 0 16 16"><g fill="var(--green)"><circle cx="8" cy="11" r="3.6"/><circle cx="3" cy="6.5" r="1.8"/><circle cx="6.3" cy="3.4" r="1.8"/><circle cx="9.7" cy="3.4" r="1.8"/><circle cx="13" cy="6.5" r="1.8"/></g></svg>Pregnancy Ultrasound</li>
      <li><svg viewBox="0 0 16 16"><g fill="var(--green)"><circle cx="8" cy="11" r="3.6"/><circle cx="3" cy="6.5" r="1.8"/><circle cx="6.3" cy="3.4" r="1.8"/><circle cx="9.7" cy="3.4" r="1.8"/><circle cx="13" cy="6.5" r="1.8"/></g></svg>Semen Freezing</li>
    </ul>
    <p class="band-text clinic">Brookfield Veterinary Specialists</p>
  </section>

  <!-- Philosophy -->
  <section class="panel panel-philosophy">
    <svg class="panel-bg" viewBox="0 0 370 690" preserveAspectRatio="none" aria-hidden="true">
      <path d="M0 150 L370 150 L370 690 L0 690Z" fill="var(--blue)"/>
      <path d="M0 150 L370 150" stroke="var(--green)" stroke-width="5"/>
    </svg>
    <div class="photo photo-pets" role="img" aria-label="Photo of a tabby kitten, a white and brown rabbit and a guinea pig sitting in a row"></div>
    <h2 class="philosophy-title">Our Practice Philosophy</h2>
    <div class="philosophy-rule"></div>
    <div class="philosophy-copy">
      <p>We are a medical service business. Our primary task is to solve our client's pet medical problems by maintaining the highest standards in veterinary medicine.</p>
      <ul class="philosophy-list">
        <li>A clean and reputable hospital that is customer service based</li>
        <li>Caring and efficient reception service</li>
        <li>High skilled and knowledgeable technicians</li>
        <li>Doctors who have a love for animals</li>
      </ul>
    </div>
    <div class="photo photo-vet" role="img" aria-label="Photo of a veterinarian in blue scrubs gently holding a small black and white dog"></div>
  </section>

</main>
</body>
</html>
```